Home Improvement Company in need of a "Banner & Billboard Design"

I'm Looking for a Banner design 4X6 With Company Logo, Phone Number, website, Credentials and services.. I picture a charcoal/matte background i also want to look like a house shape design i will upload the sample...

I'm looking for a Billboard design to target homeowners who need Roofing Services. I need logo, number, website, KLN, Credentials and a catchy title. i will like to use the same colors for branding

Target Market(s)

Homeowners, Investors,

Industry/Entity Type

Home Improvement

Font styles to use
Decorative

Colors
00a990
5c5c5c
333333

Requirements
Must have
• All Credentials, Phone number, website, logo, logo colors, services, Eye Catchy, Direct Message, Friendly feeling,
• (555) 319 - 4826
• Roofing Gutters Painting Pressure Washing Exterior Design
Nice to have
• A catchy title, A direct message to a homeowner looking for home improvement services. noticeable
Should not have
• not Busy, no

```html
<!DOCTYPE html>
<html lang="en">
<head>
<meta charset="utf-8">
<title>Ridgeline Home Exteriors – Roofing Banner</title>
<link rel="stylesheet" href="https://fonts.googleapis.com/css2?family=Great+Vibes&family=Open+Sans:wght@600;700&display=swap">
<style>
  :root {
    --teal: #00a990;
    --charcoal: #333333;
    --ridge: #3a3c3d;
    --grey: #5c5c5c;
    --orange: #f5a54a;
    --white: #ffffff;
  }
  html, body {
    margin: 0;
    width: 1200px;
    height: 1200px;
    overflow: hidden;
    background: var(--white);
    font-family: "Open Sans", Arial, sans-serif;
  }
  .canvas { position: relative; width: 1200px; height: 1200px; }
  .banner {
    position: absolute;
    left: 40px; top: 226px;
    width: 1120px; height: 748px;
    background: var(--white);
    box-shadow: 4px 5px 6px rgba(0,0,0,0.45);
    overflow: hidden;
  }
  .banner-field {
    position: absolute;
    left: 0; top: 0;
    width: 1120px; height: 670px;
    background: var(--charcoal);
    overflow: hidden;
  }
  .backdrop-roof { position: absolute; left: 0; top: 0; }
  .headline { position: absolute; left: 0; top: 0; }
  .headline text {
    font-family: "Great Vibes", cursive;
    font-size: 74px;
    fill: var(--orange);
  }
  .credential-badge {
    position: absolute;
    background: var(--white);
  }
  .credential-badge.roofing-cert { left: 26px; top: 20px; width: 204px; height: 76px; }
  .credential-badge.accreditation { left: 26px; top: 512px; width: 83px; height: 132px; }
  .brand-name {
    position: absolute;
    left: 180px; top: 300px;
    width: 510px;
    text-align: center;
    color: var(--teal);
    font-weight: 700;
    font-size: 58px;
    line-height: 1.15;
    letter-spacing: 1px;
  }
  .brand-mark {
    display: block;
    width: 74px; height: 74px;
    margin: 0 auto 22px;
    background: var(--teal);
  }
  .services { list-style: none; margin: 0; padding: 0; }
  .service {
    position: absolute;
    height: 66px;
    border-radius: 33px;
    background: var(--teal);
    color: var(--white);
    font-weight: 700;
    font-size: 35px;
    line-height: 66px;
    text-align: center;
    letter-spacing: 0.5px;
  }
  .service.wide { left: 702px; width: 402px; }
  .service.short { left: 844px; width: 250px; }
  .contact-strip {
    position: absolute;
    left: 0; top: 670px;
    width: 1120px; height: 78px;
    color: var(--orange);
    font-weight: 600;
    font-size: 37px;
    line-height: 78px;
  }
  .contact-strip .website { position: absolute; left: 16px; }
  .contact-strip .phone { position: absolute; left: 755px; }
</style>
</head>
<body>
<div class="canvas">
  <section class="banner">
    <div class="banner-field">
      <svg class="backdrop-roof" width="1120" height="670" viewBox="0 0 1120 670" aria-hidden="true">
        <polyline points="-20,470 444,110 1150,600" fill="none" stroke="var(--ridge)" stroke-width="90" stroke-linejoin="miter"/>
      </svg>

      <svg class="headline" width="1120" height="670" viewBox="0 0 1120 670">
        <text x="30" y="228" textLength="876" lengthAdjust="spacingAndGlyphs" transform="rotate(-10 30 228)">Need to Spruce up your Roof ?</text>
      </svg>

      <div class="credential-badge roofing-cert" role="img" aria-label="Certified roofing contractor badge"></div>
      <div class="credential-badge accreditation" role="img" aria-label="KLN accredited business badge"></div>

      <div class="brand-name">
        <span class="brand-mark"></span>
        Ridgeline<br>Home Exteriors
      </div>

      <ul class="services">
        <li class="service wide" style="top:127px;">EXTERIOR DESIGN</li>
        <li class="service wide" style="top:233px;">PRESSURE WASHING</li>
        <li class="service short" style="top:340px;">GUTTERS</li>
        <li class="service short" style="top:446px;">PAINTING</li>
        <li class="service short" style="top:552px;">ROOFING</li>
      </ul>
    </div>

    <footer class="contact-strip">
      <span class="website">www.ridgelinehomeexteriors.com</span>
      <span class="phone">(555) 319-4826</span>
    </footer>
  </section>
</div>
</body>
</html>
```